New Advertising Company Business Card

A two sided business card. One side with logo only and the other side with my information and maybe my logo again. Looking for something unique and creative, but not too busy. Info would include my name(Marcus Feldon), President, phone number, address, email address, and website. LOGO IS THE BLUE AND WHITE ONE.

Target Market(s)

CEO/VP Level Audience

Industry/Entity Type

Business

Contact Information for Business Card

In Description.

```html
<!DOCTYPE html>
<html lang="en">
<head>
<meta charset="utf-8">
<title>Alcove Advertising – Business Card</title>
<link href="https://fonts.googleapis.com/css2?family=Montserrat:wght@400;500;600;700&display=swap" rel="stylesheet">
<style>
  :root {
    --stage: #1c1d1e;
    --card-dark: #1a1b1c;
    --card-light: #ffffff;
    --brand-blue: #1f73c4;
    --ink: #2a2b2d;
    --ink-soft: #3a3b3e;
    --white: #ffffff;
  }
  * { margin: 0; padding: 0; box-sizing: border-box; }
  html, body {
    width: 1200px; height: 900px; overflow: hidden;
    background: var(--stage);
    font-family: "Montserrat", sans-serif;
  }
  .canvas { position: relative; width: 1200px; height: 900px; }

  .card {
    position: absolute; left: 300px; width: 600px; height: 343px;
    border-radius: 22px; overflow: hidden;
  }
  .card--front { top: 60px; background: var(--card-dark); }
  .card--back { top: 490px; background: var(--card-light); }

  /* Front */
  .front-brand {
    position: absolute; left: 0; right: 0; top: 120px;
    display: flex; align-items: center; justify-content: center; gap: 14px;
  }
  .brand-dot {
    width: 16px; height: 16px; border-radius: 50%; background: var(--brand-blue); flex: none;
  }
  .brand-name {
    font-weight: 600; font-size: 34px; letter-spacing: 3px;
    text-transform: uppercase; line-height: 1;
  }
  .front-brand .brand-name { color: var(--white); }
  .front-web {
    position: absolute; left: 0; right: 0; bottom: 44px; text-align: center;
    color: var(--white); font-size: 15px; letter-spacing: 1.5px; font-weight: 500;
  }
  .front-web .accent { color: var(--brand-blue); }

  /* Back */
  .back-brand {
    position: absolute; left: 40px; top: 66px;
    display: flex; align-items: center; gap: 12px;
  }
  .back-brand .brand-name {
    color: var(--ink); font-size: 22px; letter-spacing: 2px; line-height: 1.2;
  }
  .back-brand .brand-name span { display: block; }
  .back-brand .brand-dot { width: 12px; height: 12px; }

  .identity { position: absolute; right: 34px; top: 60px; text-align: right; }
  .identity__name {
    color: var(--brand-blue); font-weight: 600; font-size: 27px;
    text-transform: uppercase; letter-spacing: -0.3px; line-height: 1;
  }
  .identity__title {
    color: var(--ink); font-size: 15px; font-weight: 500;
    letter-spacing: 1px; margin-top: 6px; text-transform: uppercase;
  }
  .divider {
    position: absolute; left: 40px; right: 34px; top: 148px;
    height: 1.5px; background: var(--brand-blue);
  }
  .address {
    position: absolute; right: 34px; top: 166px; text-align: right;
    color: var(--ink-soft); font-size: 14px; line-height: 1.45; font-style: normal;
  }
  .contacts {
    position: absolute; left: 40px; top: 202px; list-style: none;
    color: var(--ink-soft); font-size: 15px; line-height: 1;
  }
  .contacts li { display: flex; align-items: center; gap: 12px; margin-bottom: 11px; }
  .contacts svg { width: 14px; height: 14px; flex: none; }

  .swoosh { position: absolute; left: 0; bottom: 0; width: 600px; height: 343px; }
  .back-web {
    position: absolute; right: 40px; bottom: 26px;
    color: var(--white); font-size: 15px; letter-spacing: 0.5px;
  }
</style>
</head>
<body>
<main class="canvas">

  <section class="card card--front" aria-label="Card front">
    <div class="front-brand">
      <span class="brand-dot"></span>
      <span class="brand-name">Alcove Advertising</span>
    </div>
    <p class="front-web">www.<span class="accent">alcoveads</span>.com</p>
  </section>

  <section class="card card--back" aria-label="Card back">
    <svg class="swoosh" viewBox="0 0 600 343" aria-hidden="true">
      <path d="M290 343 C 370 280, 460 250, 600 232 L600 343 Z" fill="#1a1b1c"/>
      <path d="M350 343 C 420 300, 500 272, 600 258 L600 343 Z" fill="#ffffff"/>
      <path d="M358 343 C 428 304, 505 278, 600 266 L600 343 Z" fill="#1f73c4"/>
    </svg>

    <div class="back-brand">
      <span class="brand-dot"></span>
      <span class="brand-name"><span>Alcove</span><span>Advertising</span></span>
    </div>

    <div class="identity">
      <h1 class="identity__name">Marcus Feldon</h1>
      <p class="identity__title">President</p>
    </div>

    <div class="divider"></div>

    <address class="address">
      Unit 8, The Marlow Works,<br>
      Fenwick Lane, Hartbury,<br>
      HB4 2QL
    </address>

    <ul class="contacts">
      <li>
        <svg viewBox="0 0 14 14"><rect x="3.5" y="1" width="7" height="12" rx="1.2" fill="none" stroke="#1f73c4" stroke-width="1.4"/><line x1="6" y1="11" x2="8" y2="11" stroke="#1f73c4" stroke-width="1.2"/></svg>
        +63 917 555 0142
      </li>
      <li>
        <svg viewBox="0 0 14 14"><path d="M3 1.5 L5.2 1.5 L6 4.5 L4.6 5.6 C5.4 7.4 6.6 8.6 8.4 9.4 L9.5 8 L12.5 8.8 L12.5 11 C12.5 12 11.6 12.6 10.6 12.4 C6 11.6 2.4 8 1.6 3.4 C1.4 2.4 2 1.5 3 1.5 Z" fill="#1f73c4"/></svg>
        01632 960418
      </li>
      <li>
        <svg viewBox="0 0 14 14"><rect x="1" y="3" width="12" height="8.5" rx="1" fill="none" stroke="#1f73c4" stroke-width="1.4"/><path d="M1.5 3.5 L7 8 L12.5 3.5" fill="none" stroke="#1f73c4" stroke-width="1.4"/></svg>
        hello@alcoveads.com
      </li>
    </ul>

    <p class="back-web">www.alcoveads.com</p>
  </section>

</main>
</body>
</html>
```